Business Card Design Project

We are an incubator company that helps young entrepreneur to launch new ideas into the market. We will be targeting investors or likewise; Angels, young entrepreneurs and technopreneurs.

Our logo is being tasked by artswarm to design, therefore there is no logo for now.
You can us Lanternfield Pte Ltd as the logo for the time being.

Please let us have some versions of modern and yet professional designs; for words, you can indicate e.g (address), (Title)

thanks

Target Market(s)

young entrepreneurs
angels, investors

Industry/Entity Type

Business

Colors
3176b5
ffffff

Requirements
Must have
• able to project out our name; Lanternfield
Should not have
• Nothing childish or cartoon

```html
<!DOCTYPE html>
<html lang="en">
<head>
<meta charset="utf-8">
<title>Lanternfield Business Card</title>
<link rel="stylesheet" href="https://fonts.googleapis.com/css2?family=Jost:wght@300;400;500;600&display=swap">
<style>
  :root {
    --page-bg: #8f8f8f;
    --card-blue: #00aeef;
    --ink-white: #ffffff;
    --mark-tint: rgba(255, 255, 255, 0.22);
  }
  * { box-sizing: border-box; margin: 0; padding: 0; }
  html, body {
    width: 1200px;
    height: 900px;
    overflow: hidden;
    background: var(--page-bg);
  }
  .business-card {
    position: absolute;
    left: 100px;
    top: 164px;
    width: 1000px;
    height: 572px;
    background: var(--card-blue);
    color: var(--ink-white);
    font-family: "Jost", "Century Gothic", sans-serif;
    overflow: hidden;
  }
  .holder {
    position: absolute;
    left: 230px;
    top: 130px;
    line-height: 1;
  }
  .holder-name {
    font-size: 46px;
    font-weight: 300;
    letter-spacing: 0.5px;
  }
  .holder-name strong { font-weight: 600; }
  .holder-title {
    margin-left: 70px;
    margin-top: 4px;
    font-size: 24px;
    font-weight: 300;
    letter-spacing: 1px;
  }
  .contact-list {
    position: absolute;
    left: 560px;
    top: 352px;
    list-style: none;
    font-size: 21px;
    font-weight: 300;
    letter-spacing: 1px;
    line-height: 32px;
  }
  .contact-list li:nth-child(2) { padding-left: 8px; }
  .contact-list li:nth-child(3) { padding-left: 16px; }
  .brand-name {
    position: absolute;
    right: 8px;
    top: 0;
    writing-mode: vertical-rl;
    font-size: 70px;
    font-weight: 500;
    line-height: 1;
    letter-spacing: 1px;
  }
  .mark-placeholder {
    position: absolute;
    left: 0;
    bottom: 0;
    width: 200px;
    height: 240px;
    background: var(--mark-tint);
  }
</style>
</head>
<body>
  <div class="business-card">
    <div class="holder">
      <div class="holder-name">your<strong>name</strong></div>
      <div class="holder-title">designation</div>
    </div>

    <ul class="contact-list">
      <li>email :</li>
      <li>phone :</li>
      <li>address :</li>
    </ul>

    <div class="brand-name">lanternfield</div>

    <div class="mark-placeholder" role="img" aria-label="Space for the company symbol"></div>
  </div>
</body>
</html>
```